Celebrity and Entertainment News Website Needed

Entertainment is one of the favors of Life and I am seeking a standard celebrity website which will discuss in depth news of different celebrities around globe with major focus on American Entertainers. There will be different categories of news from these regions. America, Europe, Asia, Australia and Africa. My website name is coralvista. Youthful colors should be used for the theme and designs, Users should be able to comment at the bottom of each news. Glossy pictures of well know celebrities should be used. Designers can get knowledge from http://qarvetto.com

```html
<!DOCTYPE html>
<html lang="en">
<head>
<meta charset="utf-8">
<title>coralvista — Celebrity News</title>
<link rel="stylesheet" href="https://fonts.googleapis.com/css2?family=Raleway:wght@500;600;700;800&family=Open+Sans:wght@400;600;700;800&family=Cinzel:wght@500&display=swap">
<style>
:root{
  --red:#d9141b;
  --red-deep:#b80d12;
  --yellow:#e6b325;
  --black:#0d0d0d;
  --ink:#222;
  --muted:#8a8a8a;
  --line:#e2e2e2;
  --footer:#ececec;
  --white:#fff;
}
*{margin:0;padding:0;box-sizing:border-box}
html,body{width:1200px;height:2605px;overflow:hidden;background:var(--white)}
body{position:relative;font-family:"Open Sans",sans-serif;color:var(--ink)}
.abs{position:absolute}
/* header */
.brand{left:145px;top:48px;font-family:"Cinzel",serif;font-size:34px;color:var(--red);letter-spacing:1px}
.top-ad{left:486px;top:31px;width:576px;height:70px;border:1px solid var(--line);display:flex;align-items:center}
.top-ad .ad-photo{width:286px;height:100%;background:linear-gradient(90deg,#6b5a3c,#a38a60,#3f3526)}
.top-ad .ad-cta{margin-left:34px;width:120px;height:32px;border:2px solid #6cc3d8;color:#3aa6c4;font:700 13px/28px "Open Sans",sans-serif;text-align:center}
.top-ad .ad-brand{margin-left:22px;font:600 15px/1 "Open Sans",sans-serif;color:#333}
.nav{left:0;top:120px;width:1200px;height:50px;background:var(--black)}
.nav-home{left:140px;top:0;width:105px;height:50px;background:var(--yellow);display:flex;align-items:center;justify-content:center}
.nav-item{top:0;height:50px;color:var(--white);font:600 15px/50px "Raleway",sans-serif;text-transform:uppercase}
.nav-sep{top:12px;width:1px;height:26px;background:#333}
.nav-search{left:990px;top:13px}
/* hero */
.hero{left:0;top:170px;width:1200px;height:418px;background:radial-gradient(ellipse at 70% 35%,#e9d2c0 0%,#a6857a 30%,#5a4543 60%,#2e2325 100%)}
.hero-title{left:142px;top:305px;color:var(--white);font:700 46px/1 "Raleway",sans-serif}
.hero-sub{left:142px;top:364px;color:var(--white);font:700 33px/1 "Raleway",sans-serif}
.hero-text{left:142px;top:410px;width:470px;color:var(--white);font:400 15px/1.55 "Open Sans",sans-serif}
.hero-dots{left:140px;top:463px;display:flex;gap:5px}
.hero-dots span{width:17px;height:17px;border-radius:50%;background:var(--white)}
.hero-dots span:first-child{background:transparent;border:2px solid var(--white)}
.regions{left:130px;top:544px;width:947px;height:44px;background:var(--yellow)}
.regions-label{left:0;top:0;width:195px;height:44px;background:var(--red);clip-path:polygon(0 0,100% 0,88% 100%,0 100%);color:var(--white);font:600 16px/44px "Raleway",sans-serif;padding-left:33px}
.region{top:0;color:var(--white);font:600 16px/44px "Raleway",sans-serif}
/* top news */
.section-title{font:600 24px/1 "Raleway",sans-serif;text-transform:uppercase}
.photo{background:linear-gradient(135deg,#5b4d48,#1c1818)}
.news-title{font:400 16px/1.35 "Open Sans",sans-serif;color:var(--ink)}
.news-text{font:400 11px/1.5 "Open Sans",sans-serif;color:var(--muted)}
.news-date{font:400 11px/1 "Open Sans",sans-serif;color:#555}
.play{left:603px;top:611px;width:471px;height:295px;background:linear-gradient(120deg,#2a2a2e,#5c5a5f 45%,#1a1a1c)}
/* blogs */
.blogs{left:0;top:962px;width:1200px;height:403px;background:radial-gradient(ellipse at 50% 40%,var(--red),var(--red-deep))}
.blog-card{top:1042px;width:290px;height:280px;background:var(--white)}
.blog-card .photo{width:100%;height:167px}
.blog-card h3{margin:20px 0 0 26px;font:600 16px/1 "Open Sans",sans-serif}
.blog-card p{margin:8px 26px 0;font:400 11px/1.5 "Open Sans",sans-serif;color:var(--muted)}
.blog-card small{display:block;margin:4px 0 0 26px;font-size:11px;color:#555}
/* grid */
.tile{width:212px}
.tile .photo{height:165px}
.tile h4{margin:12px 2px 0;font:400 16px/1.3 "Open Sans",sans-serif}
.tile p{margin:6px 2px 0;font:400 11px/1 "Open Sans",sans-serif;color:var(--muted)}
.tile small{display:block;margin:10px 2px 0;font-size:11px;color:#555}
/* sidebar */
.recent{left:818px;top:1415px;width:246px;height:417px;border:1px solid var(--line)}
.recent-head{height:42px;background:var(--yellow);color:var(--white);font:600 18px/42px "Raleway",sans-serif;padding-left:22px;margin:-1px -1px 0}
.recent-item{margin:0 18px;padding:14px 0 12px;border-bottom:1px solid var(--line)}
.recent-item:last-child{border:0}
.recent-item h5{font:600 12px/1.3 "Open Sans",sans-serif;text-transform:uppercase}
.recent-item p{margin-top:4px;font:400 11px/1.5 "Open Sans",sans-serif;color:var(--muted)}
.ad-cloud{left:818px;top:1845px;width:246px;height:206px;background:linear-gradient(180deg,#e01b22,#c90f15);border:1px solid #ccc}
.ad-cloud h6{margin:30px 18px 0;color:var(--white);font:800 21px/1.08 "Open Sans",sans-serif;text-transform:uppercase}
.ad-cloud .ad-foot{position:absolute;left:0;bottom:0;width:100%;height:50px;background:#7d0a0e;display:flex;align-items:center;padding:0 10px;gap:8px}
.ad-foot .dot{width:24px;height:24px;border-radius:50%;background:var(--white)}
.ad-foot .nm{color:var(--white);font:700 17px/1 "Open Sans",sans-serif}
.ad-foot .btn{margin-left:auto;background:var(--white);color:var(--red);font:800 11px/1 "Open Sans",sans-serif;padding:6px 8px}
.ad-phone{left:818px;top:2068px;width:246px;height:202px;background:#f7d80f;border:1px solid #ccc}
.ad-phone .nm{position:absolute;left:16px;top:18px;font:700 17px/1 "Open Sans",sans-serif}
.ad-phone .hd{position:absolute;left:16px;top:64px;width:140px;font:800 13px/1.15 "Open Sans",sans-serif;text-transform:uppercase}
.ad-phone .sm{position:absolute;left:16px;top:128px;width:130px;font:400 8px/1.3 "Open Sans",sans-serif}
.ad-phone .go{position:absolute;left:16px;top:158px;background:var(--black);color:var(--white);font:700 8px/1 "Open Sans",sans-serif;padding:4px 8px}
.ad-phone .device{position:absolute;left:168px;top:40px;width:58px;height:112px;border-radius:8px;background:linear-gradient(#eee,#bbb)}
.ad-phone .mdl{position:absolute;right:12px;bottom:10px;font:700 9px/1 "Open Sans",sans-serif}
/* footer */
.footer{left:0;top:2322px;width:1200px;height:233px;background:var(--footer)}
.f-col h6{font:600 16px/1 "Raleway",sans-serif;color:#555;text-transform:uppercase;margin-bottom:12px}
.f-col li{list-style:none;font:400 12px/21px "Open Sans",sans-serif;color:#666}
.social{display:flex;gap:5px;margin-top:14px}
.social span{width:24px;height:24px;border:1.5px solid #555;border-radius:50%}
.f-news p{font:400 12px/1 "Open Sans",sans-serif;color:#444;margin-bottom:10px}
.f-news .field{width:232px;height:32px;background:var(--white);font:400 11px/32px "Open Sans",sans-serif;padding-left:10px;color:#444}
.f-news .btn{display:inline-block;margin-top:8px;background:var(--black);color:var(--white);font:600 12px/32px "Open Sans",sans-serif;padding:0 20px}
.copyright{left:144px;top:2576px;font:400 11px/1 "Open Sans",sans-serif;color:#555}
</style>
</head>
<body>

<header>
  <div class="abs brand">CORALVISTA</div>
  <div class="abs top-ad">
    <div class="ad-photo" role="img" aria-label="Advertisement photo of a pianist at a piano"></div>
    <div class="ad-cta">EXPLORE NOW</div>
    <div class="ad-brand">Lumenframe</div>
  </div>
</header>

<nav class="abs nav">
  <div class="abs nav-home">
    <svg width="24" height="22" viewBox="0 0 24 22"><path d="M12 1 1 11h3v10h6v-6h4v6h6V11h3z" fill="#fff"/></svg>
  </div>
  <span class="abs nav-item" style="left:273px">News</span>
  <span class="abs nav-sep" style="left:343px"></span>
  <span class="abs nav-item" style="left:367px">Style</span>
  <span class="abs nav-sep" style="left:436px"></span>
  <span class="abs nav-item" style="left:462px">Blog</span>
  <span class="abs nav-sep" style="left:525px"></span>
  <span class="abs nav-item" style="left:551px">Red Carpet</span>
  <span class="abs nav-sep" style="left:668px"></span>
  <span class="abs nav-item" style="left:693px">Shows</span>
  <span class="abs nav-sep" style="left:775px"></span>
  <span class="abs nav-item" style="left:798px">Event</span>
  <span class="abs nav-sep" style="left:870px"></span>
  <span class="abs nav-item" style="left:895px">More</span>
  <svg class="abs nav-search" width="24" height="24" viewBox="0 0 24 24"><circle cx="10" cy="10" r="7" fill="none" stroke="#fff" stroke-width="3"/><path d="m15 15 6 6" stroke="#fff" stroke-width="3" stroke-linecap="round"/></svg>
</nav>

<section>
  <div class="abs hero" role="img" aria-label="Concert crowd with raised hands under stage lights"></div>
  <h1 class="abs hero-title">MASSA LIBERO INTERDUM</h1>
  <h2 class="abs hero-sub">INTERDUM VEL BLANDIT SED NULLA</h2>
  <p class="abs hero-text">Morbi diam mauris viverra in gravida eu mattis in ante Morbi eget arcu Morbi porta libero id ullamcorper nonummy nibh</p>
  <div class="abs hero-dots"><span></span><span></span><span></span><span></span></div>
  <div class="abs regions">
    <div class="abs regions-label">SELECT REGIONS</div>
    <span class="abs region" style="left:237px">AMERICA</span>
    <span class="abs region" style="left:362px">EUROPE</span>
    <span class="abs region" style="left:480px">ASIA</span>
    <span class="abs region" style="left:568px">AUSTRALIA</span>
    <span class="abs region" style="left:711px">AFRICA</span>
  </div>
</section>

<section>
  <h2 class="abs section-title" style="left:137px;top:612px">TOP NEWS</h2>
  <div class="abs photo" style="left:132px;top:650px;width:216px;height:137px" role="img" aria-label="Actor in a tuxedo at a premiere"></div>
  <p class="abs news-title" style="left:130px;top:792px;width:210px">Fusce tellus Sed metus augue convallis</p>
  <p class="abs news-text" style="left:130px;top:843px;width:210px">congue id euismod in elit Fusce ultricies orci ac feugiat suscipit leo massa</p>
  <span class="abs news-date" style="left:130px;top:886px">5 days ago</span>
  <div class="abs photo" style="left:366px;top:650px;width:216px;height:137px;background:linear-gradient(135deg,#caa27e,#5a4032)" role="img" aria-label="Actress smiling before reporters' microphones"></div>
  <p class="abs news-title" style="left:367px;top:796px;width:215px">Mauris vel lacus vitae felis vestibulum volutpat</p>
  <p class="abs news-text" style="left:367px;top:847px;width:215px">congue id euismod in elit Fusce ultricies orci ac feugiat suscipit leo massa</p>
  <span class="abs news-date" style="left:367px;top:890px">2 days ago</span>
  <div class="abs play" role="img" aria-label="Video of a celebrity couple arriving by limousine"></div>
  <svg class="abs" style="left:784px;top:707px" width="106" height="106" viewBox="0 0 106 106"><circle cx="53" cy="53" r="49" fill="none" stroke="#fff" stroke-width="6"/><path d="M42 32v42l34-21z" fill="#fff"/></svg>
</section>

<section>
  <div class="abs blogs"></div>
  <h2 class="abs section-title" style="left:151px;top:999px;color:#fff">FOR OUR BLOGS</h2>
  <svg class="abs" style="left:1012px;top:1012px" width="42" height="20" viewBox="0 0 42 20"><path d="M10 2 3 10l7 8M32 2l7 8-7 8" fill="none" stroke="#fff" stroke-width="2.5"/></svg>
  <article class="abs blog-card" style="left:151px">
    <div class="photo" role="img" aria-label="Couple in evening wear on the red carpet"></div>
    <h3>Pellentesque aliquam</h3>
    <p>Curabitur vel mi sit amet magna malesuada ultrices Ut nisi erat fermentum</p>
    <small>5 days ago</small>
  </article>
  <article class="abs blog-card" style="left:458px">
    <div class="photo" style="background:linear-gradient(135deg,#bbb,#333)" role="img" aria-label="Black and white shot of photographers flashing at a star"></div>
    <h3>Pellentesque aliquam</h3>
    <p>Curabitur vel mi sit amet magna malesuada ultrices Ut nisi erat fermentum</p>
    <small>5 days ago</small>
  </article>
  <article class="abs blog-card" style="left:764px">
    <div class="photo" style="background:linear-gradient(135deg,#2d3a6b,#8a1e24)" role="img" aria-label="Speaker at a podium before flags"></div>
    <h3>Pellentesque aliquam</h3>
    <p>Curabitur vel mi sit amet magna malesuada ultrices Ut nisi erat fermentum</p>
    <small>5 days ago</small>
  </article>
</section>

<section>
  <article class="abs tile" style="left:140px;top:1418px"><div class="photo" role="img" aria-label="Celebrity couple taking a selfie"></div><h4>Praesent elementum elit tellus nec ultricies sit</h4><p>Curabitur vel mi sit amet magna</p><small>5 days ago</small></article>
  <article class="abs tile" style="left:362px;top:1418px"><div class="photo" style="background:linear-gradient(180deg,#9fc3dd,#6b7c86)" role="img" aria-label="Cruise ships docked at a pier"></div><h4>Aehicula ut pulvinar ante Integer orci tellus</h4><p>Curabitur vel mi sit amet magna</p><small>5 days ago</small></article>
  <article class="abs tile" style="left:585px;top:1418px"><div class="photo" style="background:linear-gradient(180deg,#4a3a3a,#b3242a)" role="img" aria-label="Red carpet lined with velvet ropes"></div><h4>Suspendisse quam leo molestie sed luctus</h4><p>Curabitur vel mi sit amet magna</p><small>5 days ago</small></article>

  <article class="abs tile" style="left:140px;top:1720px"><div class="photo" style="background:linear-gradient(135deg,#6a5546,#1d1714)" role="img" aria-label="Actress in a sequined gown posing"></div><h4>Praesent elementum elit tellus nec ultricies sit</h4><p>Curabitur vel mi sit amet magna</p><small>5 days ago</small></article>
  <article class="abs tile" style="left:362px;top:1720px"><div class="photo" style="background:linear-gradient(135deg,#c9b59c,#2a2420)" role="img" aria-label="Blonde star among camera flashes"></div><h4>Aehicula ut pulvinar ante Integer orci tellus</h4><p>Curabitur vel mi sit amet magna</p><small>5 days ago</small></article>
  <article class="abs tile" style="left:585px;top:1720px"><div class="photo" style="background:linear-gradient(135deg,#e6d7c3,#3a302a)" role="img" aria-label="Actress in a white dress on the carpet"></div><h4>Suspendisse quam leo molestie sed luctus</h4><p>Curabitur vel mi sit amet magna</p><small>5 days ago</small></article>

  <article class="abs tile" style="left:140px;top:2013px"><div class="photo" style="background:linear-gradient(135deg,#b49a7c,#222)" role="img" aria-label="Star stepping out of a car at night"></div><h4>Praesent elementum elit tellus nec ultricies sit</h4><p>Curabitur vel mi sit amet magna</p><small>5 days ago</small></article>
  <article class="abs tile" style="left:362px;top:2013px"><div class="photo" style="background:linear-gradient(135deg,#5a2a2a,#150f0f)" role="img" aria-label="Glamorous actress in a dark gown"></div><h4>Aehicula ut pulvinar ante Integer orci tellus</h4><p>Curabitur vel mi sit amet magna</p><small>5 days ago</small></article>
  <article class="abs tile" style="left:585px;top:2013px"><div class="photo" style="background:linear-gradient(135deg,#3a3232,#a3141b)" role="img" aria-label="Couple in black suit and red dress"></div><h4>Suspendisse quam leo molestie sed luctus</h4><p>Curabitur vel mi sit amet magna</p><small>5 days ago</small></article>
</section>

<aside>
  <div class="abs recent">
    <div class="recent-head">RECENT POSTS</div>
    <div class="recent-item"><h5>Etiam eu urna sed port</h5><p>odio Cras a ante vitae enim iaculis aliquam Mauris nunc quam venenatis</p></div>
    <div class="recent-item"><h5>Duis non nunc nulla</h5><p>odio Cras a ante vitae enim iaculis aliquam Mauris nunc quam venenatis</p></div>
    <div class="recent-item"><h5>Vivamus porttitor nequ</h5><p>odio Cras a ante vitae enim iaculis aliquam Mauris nunc quam venenatis nec euismod sit amet egestas</p></div>
    <div class="recent-item"><h5>Praesent elementum elit</h5><p>odio Cras a ante vitae enim iaculis aliquam Mauris nunc quam</p></div>
  </div>
  <div class="abs ad-cloud">
    <h6>Build powerful voice &amp; SMS apps in the cloud</h6>
    <div class="ad-foot"><span class="dot"></span><span class="nm">relaycast</span><span class="btn">TRY IT FREE</span></div>
  </div>
  <div class="abs ad-phone">
    <span class="nm">Brightwave</span>
    <span class="hd">Now in white. The Nova X4 LTE only from Brightwave.</span>
    <span class="sm">the only national carrier with truly unlimited data.</span>
    <span class="go">GET IT NOW</span>
    <span class="device"></span>
    <span class="mdl">NOVA X4 LTE</span>
  </div>
</aside>

<footer>
  <div class="abs footer"></div>
  <div class="abs f-col" style="left:148px;top:2378px"><h6>Company</h6><ul><li>Home</li><li>Gadgets</li><li>Category</li><li>Breaking News</li></ul></div>
  <div class="abs f-col" style="left:306px;top:2378px"><h6>Sublinks</h6><ul><li>Phasellus felis</li><li>celerisque</li><li>Tempus eget</li><li>Lobortis</li></ul></div>
  <div class="abs f-col" style="left:466px;top:2378px"><h6>Latest Posts</h6><ul><li>Phasellus felis</li><li>Dolor celerisque</li><li>Tempus eget</li><li>Lobortis</li></ul></div>
  <div class="abs f-col" style="left:646px;top:2378px"><h6>Resources</h6><ul><li>Support</li><li>Blog</li><li>News</li><li>FAQ</li></ul>
    <div class="social"><span></span><span></span><span></span><span></span></div></div>
  <div class="abs f-col f-news" style="left:796px;top:2378px"><h6>Newsletter Subscribe</h6><p>Please sign up here for latest offers.</p><div class="field">email address</div><span class="btn">SUBSCRIBE</span></div>
  <p class="abs copyright">© 2016 Company Name &nbsp;All right reserved &nbsp;Term of Use</p>
</footer>

</body>
</html>
```